Small Business Consulting Firm Needs Business Card Design

Need a sleek modern business card with 2 sides matching the colors of our logo. We will be placing these with a mailer we are sending out. These business cards will only ever be given to business owners. We operate helping businesses who are struggling with cash flow or finances. If the green and blue design needs to be moved to the right of "Harborline Crest Consulting" for aesthetic purposes that is ok. We will need an editable file if possible. We would like to include the reps name, email, website, and phone number. For now just use Peter Vance, pvance@harborlinecrest.com, www.harborlinecrest.com, and 833-555-0172.

```html
<!DOCTYPE html>
<html lang="en">
<head>
<meta charset="utf-8">
<title>Harborline Crest Consulting – Business Card</title>
<link rel="stylesheet" href="https://fonts.googleapis.com/css2?family=Maven+Pro:wght@400;500;700&display=swap">
<style>
  :root {
    --page-bg: #161616;
    --card-bg: #131313;
    --card-tint: #1a1c1d;
    --text-light: #f2f2f2;
    --brand-green: #6db33f;
    --brand-blue: #0b7dc1;
    --muted: #9a9a9a;
  }
  * { box-sizing: border-box; margin: 0; padding: 0; }
  html, body {
    width: 1200px; height: 1020px; overflow: hidden;
    background: var(--page-bg);
    font-family: "Maven Pro", sans-serif;
    color: var(--text-light);
  }
  .canvas { position: relative; width: 1200px; height: 1020px; }
  .card {
    position: absolute; left: 272px; width: 656px; height: 374px;
    background: var(--card-bg); overflow: hidden;
    box-shadow: 0 14px 30px rgba(0,0,0,0.45);
  }
  .card--front { top: 88px; }
  .card--back { top: 517px; }

  .front__accent {
    position: absolute; left: 367px; top: 82px; width: 212px; height: 212px;
    background: var(--card-tint);
  }
  .wordmark { position: absolute; left: 20px; top: 58px; display: flex; align-items: center; gap: 11px; }
  .wordmark__square { width: 30px; height: 30px; background: var(--brand-green); }
  .wordmark__name { font-weight: 500; font-size: 22px; letter-spacing: 0.06em; line-height: 1; color: var(--text-light); }
  .wordmark__sub { display: block; font-size: 11px; letter-spacing: 0.5em; margin-top: 6px; }

  .address { position: absolute; left: 19px; top: 205px; font-size: 18px; line-height: 24px; }
  .divider { position: absolute; left: 20px; top: 258px; width: 53px; height: 2px; background: var(--brand-green); }
  .contacts { position: absolute; left: 19px; top: 269px; list-style: none; }
  .contacts li { display: flex; align-items: center; gap: 9px; font-size: 18px; height: 27px; }
  .contacts svg { width: 14px; height: 14px; fill: var(--brand-blue); flex: none; }
  .contacts .highlight { color: var(--brand-green); }

  .rep { position: absolute; right: 18px; top: 262px; text-align: right; }
  .rep__name { font-weight: 700; font-size: 27px; color: var(--brand-blue); line-height: 1.1; }
  .rep__title { font-size: 19px; color: var(--brand-green); margin-top: 3px; }

  .back__mark {
    position: absolute; inset: 0; display: flex; flex-direction: column;
    align-items: center; justify-content: center; gap: 18px;
  }
  .back__square { width: 70px; height: 70px; background: var(--brand-green); }
  .back__name { font-weight: 500; font-size: 26px; letter-spacing: 0.08em; color: var(--text-light); text-align: center; }
  .back__name span { display: block; font-size: 13px; letter-spacing: 0.5em; margin-top: 8px; }
</style>
</head>
<body>
<main class="canvas">
  <section class="card card--front" aria-label="Business card front">
    <div class="front__accent"></div>

    <div class="wordmark">
      <div class="wordmark__square"></div>
      <div class="wordmark__name">HARBORLINE CREST<span class="wordmark__sub">CONSULTING</span></div>
    </div>

    <address class="address" style="font-style:normal">
      4410-215 Harbour Row<br>Vancouver, BC, V6B 0Z9
    </address>
    <div class="divider"></div>

    <ul class="contacts">
      <li>
        <svg viewBox="0 0 24 24" aria-hidden="true"><path d="M6.6 10.8a15.1 15.1 0 0 0 6.6 6.6l2.2-2.2a1 1 0 0 1 1-.25 11.4 11.4 0 0 0 3.6.57 1 1 0 0 1 1 1V20a1 1 0 0 1-1 1A17 17 0 0 1 3 4a1 1 0 0 1 1-1h3.5a1 1 0 0 1 1 1c0 1.25.2 2.45.57 3.57a1 1 0 0 1-.25 1z"/></svg>
        833-555-0172
      </li>
      <li>
        <svg viewBox="0 0 24 24" aria-hidden="true"><path d="M2 5h20v14H2z M2 5l10 8 10-8" /><path d="M3 6l9 7 9-7v-.5H3z" fill="#131313"/></svg>
        pvance@harborlinecrest.com
      </li>
      <li>
        <svg viewBox="0 0 24 24" aria-hidden="true"><circle cx="12" cy="12" r="10"/><path d="M7 6c2 1 3 3 2 5s-3 1-3 4M15 4c-1 2 1 3 3 4M14 20c0-2 1-4 3-4" stroke="#131313" stroke-width="2" fill="none"/></svg>
        <span>www.<span class="highlight">harborlinecrest</span>.com</span>
      </li>
    </ul>

    <div class="rep">
      <div class="rep__name">Peter Vance</div>
      <div class="rep__title">Owner</div>
    </div>
  </section>

  <section class="card card--back" aria-label="Business card back">
    <div class="back__mark">
      <div class="back__square"></div>
      <div class="back__name">HARBORLINE CREST<span>CONSULTING</span></div>
    </div>
  </section>
</main>
</body>
</html>
```